Kestrel Bread Ingredients

Ingredients list/einkorn info. We are looking to improve a 5.5 x 8.5" double sided handout (2 per 8.5 x 11" piece of paper) to hand out with bread and for marketing. Or skinnier 3 per piece of paper? Or suggest a better format. Also to be used in social media and web. And possibly a banner.

Target Market(s)

Healthy, intelligent, yoga, athletic, wealthy

Industry/Entity Type

Bakery

Font styles to use
Sans Serif
Other font styles liked:
• simple readable attractive

Requirements
Must have
• Display the value (and uniqueness) of ingredients
Nice to have
• Well presented info with instant visual appeal. Choose between the 2 logos which you like most. Let us know if you want more photos.
Should not have
• Ornate frills

```html
<!DOCTYPE html>
<html lang="en">
<head>
<meta charset="utf-8">
<title>Kestrel Bread – Ingredients Handout</title>
<link rel="stylesheet" href="https://fonts.googleapis.com/css2?family=Cinzel:wght@700&family=Crimson+Text:wght@400;700&display=swap">
<style>
  :root {
    --frame: #464646;
    --ink-blue: #294a8c;
    --ink-body: #2f2620;
    --cream: #f5e6c6;
    --cream-light: #f8efd9;
    --rust: #e08a4a;
    --crumb-light: #b88664;
    --crumb-dark: #5a3322;
  }
  * { box-sizing: border-box; margin: 0; padding: 0; }
  html, body { width: 927px; height: 1200px; overflow: hidden; background: var(--frame); }
  body { position: relative; font-family: "Crimson Text", Georgia, serif; color: var(--ink-body); }

  .panel { position: absolute; left: 53px; width: 821px; height: 354px; overflow: hidden; }
  .panel--cover { top: 53px; background: radial-gradient(ellipse at 35% 40%, var(--cream-light) 0%, var(--cream) 60%, #ead3a8 100%); }
  .panel--ingredients { top: 423px; background: radial-gradient(ellipse at 40% 50%, var(--cream-light) 0%, #f2dcb2 55%, var(--rust) 135%); }
  .panel--einkorn { top: 792px; background: radial-gradient(ellipse at 35% 45%, var(--cream-light) 0%, #f2dcb2 55%, var(--rust) 135%); }

  .heading { font-family: "Cinzel", "Times New Roman", serif; font-weight: 700; color: var(--ink-blue); position: absolute; white-space: nowrap; }

  /* cover */
  .brand-mark { position: absolute; left: 148px; top: 62px; display: flex; align-items: center; gap: 8px; }
  .brand-mark__dot { width: 14px; height: 14px; border-radius: 50%; background: var(--ink-blue); }
  .brand-mark__name { font-family: "Cinzel", "Times New Roman", serif; font-weight: 700; font-size: 26px; color: var(--ink-blue); }
  .cover-title { left: 0; width: 460px; top: 200px; text-align: center; font-size: 32px; line-height: 36px; }
  .contact { position: absolute; left: 28px; top: 316px; display: flex; align-items: center; gap: 14px; font-size: 19px; }
  .contact__item { display: flex; align-items: center; gap: 6px; }
  .photo { position: absolute; }
  .photo--slices { left: 422px; top: 0; width: 399px; height: 354px; background: linear-gradient(150deg, #f3e9d8 0%, var(--crumb-light) 30%, #8a5a3e 65%, var(--crumb-dark) 100%); }

  /* ingredients */
  .tagline { top: 26px; left: 27px; font-size: 27px; letter-spacing: 0.5px; }
  .subline { position: absolute; top: 58px; left: 27px; font-size: 15px; }
  .item { position: absolute; display: flex; gap: 10px; width: 220px; }
  .item__icon { flex: none; width: 37px; height: 37px; margin-top: 1px; }
  .item__label { font-weight: 400; text-transform: uppercase; font-size: 13px; line-height: 15px; }
  .item__text { font-size: 13.5px; line-height: 15.5px; }
  .item__note { font-size: 11.5px; line-height: 13.5px; }
  .item__group + .item__group { margin-top: 12px; }
  .item--grains { left: 27px; top: 104px; }
  .item--seeds { left: 27px; top: 204px; }
  .item--adapt { left: 276px; top: 104px; }
  .item--with { left: 276px; top: 195px; }
  .tolerance { position: absolute; left: 27px; top: 304px; font-weight: 700; font-size: 13.5px; line-height: 15.5px; }
  .photo--loaf { left: 504px; top: 60px; width: 317px; height: 275px; border-radius: 50% 45% 48% 50%; background: radial-gradient(ellipse at 45% 40%, #9a6a4a 0%, #6e4230 55%, #4a2a1e 100%); }

  /* einkorn */
  .einkorn-title { top: 24px; left: 22px; font-size: 27px; }
  .einkorn-intro { position: absolute; left: 22px; top: 59px; font-size: 15px; line-height: 18px; }
  .einkorn-label { position: absolute; left: 22px; top: 110px; font-size: 14px; text-transform: uppercase; }
  .facts { position: absolute; left: 73px; top: 135px; width: 420px; list-style: none; font-size: 13px; line-height: 15.5px; }
  .facts li { position: relative; padding-left: 25px; }
  .facts li::before { content: ""; position: absolute; left: 0; top: 4px; width: 8px; height: 8px; border-radius: 50%; background: var(--ink-blue); }
  .einkorn-note { position: absolute; left: 22px; top: 312px; font-weight: 700; font-size: 13px; }
  .photo--wheat { left: 470px; top: 0; width: 200px; height: 354px; background: linear-gradient(160deg, rgba(255,250,235,0.7), rgba(240,220,190,0)); }
  .photo--roll { left: 562px; top: 31px; width: 259px; height: 323px; border-radius: 50% 0 0 45%; background: radial-gradient(ellipse at 45% 40%, #a07458 0%, #6a4230 55%, #3e2419 100%); }
</style>
</head>
<body>

<section class="panel panel--cover">
  <div class="brand-mark"><span class="brand-mark__dot"></span><span class="brand-mark__name">Kestrel Bread</span></div>
  <h1 class="heading cover-title">The Transformation<br>of Bread</h1>
  <div class="contact">
    <span class="contact__item">
      <svg width="24" height="24" viewBox="0 0 24 24" fill="none" stroke="#294a8c" stroke-width="1.6"><path d="M6 3l3 4-2 2c1 3 4 6 7 7l2-2 4 3-2 3C10 20 4 14 3 5z"/></svg>
      406-555-0148
    </span>
    <span class="contact__item">
      <svg width="24" height="24" viewBox="0 0 24 24" fill="none" stroke="#294a8c" stroke-width="1.4"><circle cx="12" cy="12" r="10"/><ellipse cx="12" cy="12" rx="4.5" ry="10"/><path d="M2 12h20M4 7h16M4 17h16"/></svg>
      hello@kestrelbread.com
    </span>
  </div>
  <div class="photo photo--slices" role="img" aria-label="Photo of sliced marbled ancient-grain bread"></div>
</section>

<section class="panel panel--ingredients">
  <h2 class="heading tagline">Nutritious &nbsp;•&nbsp; Digestible &nbsp;•&nbsp; Delicious</h2>
  <p class="subline">An alternative to the mutated genetics of modern wheat</p>

  <div class="item item--grains">
    <svg class="item__icon" viewBox="0 0 40 40" fill="none" stroke="#294a8c" stroke-width="2"><circle cx="20" cy="20" r="18"/><path d="M20 30V16M20 20c-6 0-8-4-8-8 5 0 8 3 8 8zM20 18c0-6 4-8 8-8 0 5-3 8-8 8z"/></svg>
    <div>
      <p class="item__label">Sprouted grains:</p>
      <p class="item__text">Einkorn, spelt, and a touch of heritage rye</p>
      <p class="item__note">(Organically grown on family farms in Winthrop, Washington and Teton Valley, Idaho)</p>
    </div>
  </div>

  <div class="item item--seeds">
    <svg class="item__icon" viewBox="0 0 40 40" fill="none" stroke="#294a8c" stroke-width="2"><circle cx="20" cy="20" r="18"/><ellipse cx="15" cy="16" rx="4" ry="6" transform="rotate(-30 15 16)"/><ellipse cx="25" cy="16" rx="4" ry="6" transform="rotate(30 25 16)"/><ellipse cx="20" cy="26" rx="4" ry="6" transform="rotate(90 20 26)"/></svg>
    <div>
      <p class="item__label">Seeds:</p>
      <p class="item__text">Amaranth, sprouted pumpkin seeds, sprouted quinoa, chia seeds, flaxseed, hemp hearts, sprouted sunflowers seeds</p>
    </div>
  </div>

  <div class="item item--adapt">
    <svg class="item__icon" viewBox="0 0 40 40" fill="none" stroke="#294a8c" stroke-width="2"><circle cx="20" cy="20" r="18"/><path d="M10 20h20c0 6-4 9-10 9s-10-3-10-9zM16 29v2h8v-2M15 18c0-4 2-6 5-7M20 18c0-4 3-6 6-6"/></svg>
    <div>
      <div class="item__group">
        <p class="item__label">Adaptogens:</p>
        <p class="item__text">Ashwaganda, Maca root</p>
      </div>
      <div class="item__group">
        <p class="item__label">Mushroom extracts:</p>
        <p class="item__text">Lions mane, cordycept</p>
      </div>
    </div>
  </div>

  <div class="item item--with">
    <svg class="item__icon" viewBox="0 0 40 40" fill="none" stroke="#294a8c" stroke-width="2"><circle cx="20" cy="20" r="18"/><rect x="11" y="14" width="7" height="14" rx="1"/><rect x="20" y="18" width="9" height="10" rx="1"/><path d="M12 14v-3h5v3"/></svg>
    <div>
      <p class="item__label">With:</p>
      <p class="item__text">Montana glacier well water, Cacao, MCT oil, psyilium husk, Himalayan sea salt, trace minerals, &nbsp;love</p>
    </div>
  </div>

  <p class="tolerance">This bread is well tolerated by people with gluten sensitivities.<br>(not for celiac disease)</p>
  <div class="photo photo--loaf" role="img" aria-label="Photo of a round marbled cacao bread loaf"></div>
</section>

<section class="panel panel--einkorn">
  <div class="photo photo--wheat" role="img" aria-label="Faint illustration of wheat stalks"></div>
  <h2 class="heading einkorn-title">Einkorn Grain vs 'Modern Wheat'</h2>
  <p class="einkorn-intro">Einkorn is the original, non-altered wheat grain.<br>It's genetic purity is over 10,000 years old.</p>
  <p class="einkorn-label">Einkorn is:</p>
  <ul class="facts">
    <li>25% higher in protein and lower in carbohydrates than modern wheat</li>
    <li>3-4 times more beta-carotene</li>
    <li>2 times more vitamin A</li>
    <li>4 times more antioxidants lutein and riboflavin.</li>
    <li>5-6 times more expensive $$$</li>
    <li>richer in carotenoids, B vitamins, and essential and trace minerals</li>
    <li>non-processed, non-hybridized, non-GMO, non- mutated and has a low glycemic load, meaning it won't spike your blood sugar level.</li>
    <li>and it tastes better.</li>
  </ul>
  <p class="einkorn-note">Einkorn lacks the gluten proteins that trigger symptoms of gluten sensitivity.</p>
  <div class="photo photo--roll" role="img" aria-label="Photo of a round marbled einkorn loaf"></div>
</section>

</body>
</html>
```